Business Cards

The name of our firm is "Bayfield Insurance adjusters"
We separate ourselves from all other public adjusters because most of us worked for the insurance companies so we understand their games.
As Insurance adjusters we represent the Insured, not the insurance companies. Our # 1 priority is to handle the entire claim process as seamless as possible on behalf of the homeowner/business owner so they don't have to deal with the hassles and headaches. Just as the logo your team designed, I want the cards to stand out from everyone elses. I also want the cards to help better understand our services and Value on hiring us and value that we can offer.
I uploaded the logo whenever I created the project. I don't see an option on re uploading the logo anywhere. Any advise??

```html
<!DOCTYPE html>
<html lang="en">
<head>
<meta charset="utf-8">
<title>Bayfield Insurance Adjusters – Business Cards</title>
<link href="https://fonts.googleapis.com/css2?family=Open+Sans:ital,wght@0,400;0,600;0,700;1,400;1,700&display=swap" rel="stylesheet">
<style>
  :root {
    --stage: #3a3a3c;
    --navy: #1f3f95;
    --royal: #2a4aa8;
    --ocean: #0b5a8e;
    --ink: #1c1c1c;
    --paper: #ffffff;
    --accent: #0a5fa3;
  }
  * { margin: 0; padding: 0; box-sizing: border-box; }
  html, body { width: 1200px; height: 900px; overflow: hidden; }
  body {
    background: var(--stage);
    font-family: "Open Sans", Arial, sans-serif;
    position: relative;
  }
  .card {
    position: absolute;
    left: 320px;
    width: 560px;
    height: 320px;
    border-radius: 22px;
    overflow: hidden;
  }
  .card-front { top: 80px; background: var(--paper); }
  .card-back {
    top: 500px;
    background: linear-gradient(135deg, var(--royal) 0%, var(--navy) 45%, var(--ocean) 100%);
    color: var(--paper);
  }

  /* front */
  .front-tab {
    position: absolute; left: 0; top: 0;
    width: 10px; height: 130px;
    background: var(--accent);
  }
  .front-artwork { position: absolute; inset: 0; }
  .brand {
    position: absolute;
    display: flex; align-items: center; gap: 8px;
    font-weight: 700; font-size: 15px; letter-spacing: 0.5px;
    text-transform: uppercase;
    white-space: nowrap;
  }
  .brand-mark { width: 14px; height: 14px; flex: none; }
  .brand-front { left: 40px; top: 40px; color: var(--accent); }
  .brand-front .brand-mark { background: var(--accent); }
  .contact-list {
    position: absolute; left: 40px; top: 120px;
    list-style: none; color: var(--ink);
  }
  .contact-list li {
    display: flex; align-items: center; gap: 10px;
    font-size: 13px; line-height: 24px;
  }
  .contact-list .contact-name { font-weight: 600; font-size: 16px; }
  .contact-icon { width: 13px; height: 13px; flex: none; fill: var(--ink); }

  /* back */
  .back-tab {
    position: absolute; left: 0; top: 26px;
    width: 8px; height: 110px;
    background: var(--paper);
  }
  .services { position: absolute; left: 44px; top: 30px; }
  .services-title {
    font-weight: 700; font-style: italic;
    font-size: 15px; text-transform: uppercase; margin-bottom: 6px;
  }
  .services-list { list-style: none; font-style: italic; font-size: 13px; line-height: 19px; }
  .services-list li::before { content: "▾"; font-size: 9px; margin-right: 5px; }
  .brand-back { right: 44px; bottom: 48px; color: var(--paper); }
  .brand-back .brand-mark { background: var(--paper); }
</style>
</head>
<body>

<section class="card card-front" aria-label="Business card front">
  <svg class="front-artwork" viewBox="0 0 560 320" role="img" aria-label="Wolf silhouette filled with a blue circuit-board and globe illustration">
    <defs>
      <linearGradient id="front-wave" x1="0" y1="0" x2="1" y2="1">
        <stop offset="0" stop-color="#2b4fb0"/>
        <stop offset="1" stop-color="#0b5a8e"/>
      </linearGradient>
    </defs>
    <path d="M560 0 L430 0 C400 40 370 70 380 120 C390 170 360 200 370 250 C380 290 410 310 420 320 L560 320 Z" fill="url(#front-wave)"/>
  </svg>
  <div class="front-tab"></div>
  <div class="brand brand-front"><span class="brand-mark"></span>Bayfield Insurance Adjusters</div>
  <ul class="contact-list">
    <li class="contact-name">
      <svg class="contact-icon" viewBox="0 0 12 12"><circle cx="6" cy="3.5" r="2.8"/><path d="M0.5 12 C0.5 7.5 11.5 7.5 11.5 12 Z"/></svg>Evan Calloway
    </li>
    <li>
      <svg class="contact-icon" viewBox="0 0 12 12"><path d="M2.5 0.5 L4.5 0.5 L5.2 3.5 L3.8 4.6 C4.5 6.2 5.8 7.5 7.4 8.2 L8.5 6.8 L11.5 7.5 L11.5 9.5 C11.5 10.6 10.6 11.5 9.5 11.5 C4.5 11.5 0.5 7.5 0.5 2.5 C0.5 1.4 1.4 0.5 2.5 0.5 Z"/></svg>555-014-2270
    </li>
    <li>
      <svg class="contact-icon" viewBox="0 0 12 12"><path d="M0.5 2 H11.5 V10 H0.5 Z M1.5 3 L6 6.5 L10.5 3" fill="none" stroke="#1c1c1c" stroke-width="1"/></svg>claims@bayfieldadj.com
    </li>
    <li>
      <svg class="contact-icon" viewBox="0 0 12 12"><circle cx="6" cy="6" r="5.5"/></svg>bayfieldadj.com
    </li>
  </ul>
</section>

<section class="card card-back" aria-label="Business card back">
  <div class="back-tab"></div>
  <div class="services">
    <h2 class="services-title">Our Services</h2>
    <ul class="services-list">
      <li>Lorem Ipsum 1</li>
      <li>Lorem Ipsum 2</li>
      <li>Lorem Ipsum 3</li>
      <li>Lorem Ipsum 4</li>
      <li>Lorem Ipsum 5</li>
      <li>Lorem Ipsum 6</li>
      <li>Lorem Ipsum 7</li>
      <li>Lorem Ipsum 8</li>
    </ul>
  </div>
  <div class="brand brand-back"><span class="brand-mark"></span>Bayfield Insurance Adjusters</div>
</section>

</body>
</html>
```